IT Company needs a Wordpress Web Design

We need a wordpress website for a new IT Company called 'RJ Systemworks'. We develop educational software for Middle and High School Students and Staff. Our initial product is DeskRoute - a web app that allows School Counselors to track information about the students that they see. We would like to see modern designs that include the company logo and the DeskRoute logo

Target Market(s)

Educators

Industry/Entity Type

Information Technology

Coding

Coded - Design and coding required

Number of Pages Required

1 page

Font styles to use
Sans Serif

Requirements
Must have
• Must be able to use WordPress
Should not have
• No Flash

```html
<!DOCTYPE html>
<html lang="en">
<head>
<meta charset="utf-8">
<title>RJ Systemworks — Educational Software</title>
<link href="https://fonts.googleapis.com/css2?family=Mulish:wght@300;400;600;700;800&display=swap" rel="stylesheet">
<style>
:root{
  --blue:#4a8ac6;
  --blue-dark:#3b78b4;
  --ink:#333438;
  --text:#5f6064;
  --muted:#8a8b8f;
  --red:#c8202e;
  --light:#f5f5f5;
  --line:#e6e6e6;
  --footer:#3d3d40;
  --footer-bar:#303033;
  --footer-text:#c9c9cc;
  --white:#ffffff;
}
*{margin:0;padding:0;box-sizing:border-box}
html,body{width:1200px;height:2853px;overflow:hidden}
body{font-family:"Mulish",Arial,sans-serif;color:var(--text);background:var(--white);position:relative}
a{color:inherit;text-decoration:none}

/* header */
.site-header{position:absolute;top:0;left:0;width:1200px;height:116px;background:var(--white);z-index:3}
.brand-disc{position:absolute;left:92px;top:-70px;width:200px;height:245px;border-radius:0 0 100px 100px;background:var(--white)}
.brand{position:absolute;left:120px;top:40px;display:flex;align-items:center;gap:10px;font-size:22px;font-weight:800;color:var(--blue);letter-spacing:.5px}
.brand-mark{width:22px;height:22px;background:var(--blue)}
.main-nav{position:absolute;right:100px;top:50px;display:flex;gap:46px;font-size:14px;color:#55565a;text-transform:uppercase;letter-spacing:.3px}
.main-nav .active{color:var(--blue);position:relative}
.main-nav .active::after{content:"";position:absolute;left:0;right:0;bottom:-12px;height:2px;background:var(--blue)}

/* hero */
.hero{position:absolute;top:116px;left:0;width:1200px;height:574px;overflow:hidden;
  background:linear-gradient(100deg,#6d7074 0%,#9a9c9f 35%,#c4c4c2 60%,#a39a92 80%,#8b8580 100%)}
.hero-title{position:absolute;top:150px;width:100%;text-align:center;color:var(--white);font-size:76px;font-weight:400;letter-spacing:1px}
.hero-sub{position:absolute;top:236px;width:100%;text-align:center;color:#f2f2f2;font-size:25px;font-weight:300}
.btn-solid{position:absolute;left:489px;top:297px;width:223px;height:50px;background:var(--blue);color:var(--white);font-size:22px;font-weight:600;display:flex;align-items:center;justify-content:center;letter-spacing:.5px}
.slider-arrow{position:absolute;top:204px;width:46px;height:46px;border-radius:50%;background:rgba(255,255,255,.25);border:1px solid rgba(255,255,255,.35)}
.slider-arrow.prev{left:28px}.slider-arrow.next{right:28px}
.slider-arrow svg{position:absolute;left:15px;top:13px}
.hero-curve{position:absolute;left:400px;top:544px;width:400px;height:120px;border-radius:50%;background:var(--white)}

/* intro */
.product-intro{position:absolute;top:690px;left:0;width:1200px;height:315px;text-align:center}
.product-logo{position:absolute;top:12px;left:0;width:100%;display:flex;justify-content:center;align-items:center;gap:12px;font-size:36px;font-weight:800;color:var(--red);letter-spacing:.5px}
.product-logo .mark{width:28px;height:28px;background:var(--red)}
.intro-copy{position:absolute;top:106px;left:140px;width:920px;font-size:14px;line-height:23px;color:var(--text)}
.intro-copy p+p{margin-top:20px}

/* about */
.about{position:absolute;top:1005px;left:0;width:1200px;height:446px;
  background:linear-gradient(90deg,rgba(74,138,198,.93),rgba(74,138,198,.88)),linear-gradient(100deg,#2c4a6a,#5a84b0 50%,#3a5d82)}
.about-photo{position:absolute;inset:0}
.about h2{position:absolute;top:56px;width:100%;text-align:center;color:var(--white);font-size:52px;font-weight:300;letter-spacing:1px}
.about-lead{position:absolute;top:138px;left:180px;width:840px;text-align:center;color:var(--white);font-size:31px;font-weight:300;line-height:44px}
.btn-outline{position:absolute;left:488px;top:287px;width:224px;height:53px;border:1px solid rgba(255,255,255,.85);color:var(--white);font-size:22px;font-weight:300;display:flex;align-items:center;justify-content:center}

/* pricing */
.pricing{position:absolute;top:1451px;left:0;width:1200px;height:664px}
.section-title{position:absolute;width:100%;text-align:center;color:var(--ink);font-size:38px;font-weight:300;letter-spacing:.5px}
.pricing .section-title{top:56px}
.plan{position:absolute;top:145px;width:416px;height:450px;border:1px solid var(--line);background:var(--white)}
.plan.school{left:158px}.plan.district{left:621px}
.plan-head{height:88px;background:var(--blue);color:var(--white);font-size:24px;font-weight:600;display:flex;align-items:center;justify-content:center}
.plan-price{height:146px;border-bottom:1px solid var(--line);display:flex;align-items:center;justify-content:center;color:var(--ink)}
.plan-price .amount{font-size:72px;font-weight:800;letter-spacing:-1px}
.plan-price .unit{font-size:12px;font-weight:600;margin-top:28px;margin-left:4px}
.plan-features{list-style:none;padding:34px 0 0 38px;font-size:12.5px;color:var(--text)}
.plan-features li{display:flex;align-items:center;gap:10px;height:30px}
.plan-features svg{flex:none}

/* faq */
.faq{position:absolute;top:2115px;left:0;width:1200px;height:405px;background:var(--light)}
.faq .section-title{top:42px}
.faq-col{position:absolute;top:148px;width:230px}
.faq-col.what{left:100px}.faq-col.why{left:365px}.faq-col.how{left:630px}.faq-col.who{left:887px}
.faq-label{display:flex;align-items:center;gap:10px;font-size:18px;color:var(--ink);text-transform:uppercase;margin-bottom:16px}
.faq-label .qbox{width:28px;height:20px;border:1px solid var(--red);color:var(--red);font-size:13px;font-weight:700;display:flex;align-items:center;justify-content:center}
.faq-q{color:var(--blue);font-size:13.5px;line-height:17px;margin-bottom:2px}
.faq-a{font-size:11.5px;line-height:17px;color:#444;margin-bottom:14px}

/* footer */
.site-footer{position:absolute;top:2520px;left:0;width:1200px;height:273px;background:var(--footer);color:var(--footer-text)}
.footer-col{position:absolute;top:38px}
.footer-col h4{font-size:15px;font-weight:400;color:var(--white);text-transform:uppercase;margin-bottom:14px}
.footer-col ul{list-style:none;font-size:12px;line-height:27.5px}
.col-links{left:100px}.col-news{left:244px;width:280px}.col-info{left:615px}.col-why{left:810px}.col-contact{left:950px}
.col-news p{font-size:11.5px;line-height:17px;margin-bottom:16px}
.news-input{width:242px;height:42px;background:var(--white);color:#999;font-size:11px;padding:14px 12px}
.news-btn{margin-top:15px;width:94px;height:42px;background:var(--blue);color:var(--white);font-size:12px;display:flex;align-items:center;justify-content:center}
.footer-divider{position:absolute;top:38px;width:1px;height:180px;background:#4c4c50}
.col-contact li{display:flex;align-items:center;gap:8px}
.col-contact .indent{padding-left:5px}
.footer-bar{position:absolute;top:2793px;left:0;width:1200px;height:60px;background:var(--footer-bar);color:var(--footer-text);font-size:12px}
.footer-bar .copy{position:absolute;left:100px;top:22px}
.social{position:absolute;right:100px;top:19px;display:flex;align-items:center;gap:22px}
.social .dot{width:10px;height:10px;border-radius:50%;background:var(--footer-text)}
</style>
</head>
<body>

<header class="site-header">
  <div class="brand-disc"></div>
  <a class="brand" href="#"><span class="brand-mark"></span>RJ Systemworks</a>
  <nav class="main-nav">
    <a class="active" href="#">Home</a>
    <a href="#">About Us</a>
    <a href="#">Our Services</a>
    <a href="#">Blog</a>
    <a href="#">Partners</a>
    <a href="#">Contact Us</a>
  </nav>
</header>

<section class="hero">
  <div role="img" aria-label="Photo of hands typing on a white keyboard" style="position:absolute;inset:0"></div>
  <a class="slider-arrow prev" href="#"><svg width="14" height="20" viewBox="0 0 14 20"><path d="M11 2 3 10l8 8" fill="none" stroke="#fff" stroke-width="2"/></svg></a>
  <a class="slider-arrow next" href="#"><svg width="14" height="20" viewBox="0 0 14 20"><path d="M3 2l8 8-8 8" fill="none" stroke="#fff" stroke-width="2"/></svg></a>
  <h1 class="hero-title">RJ SYSTEMWORKS</h1>
  <p class="hero-sub">We develop educational software for Middle and High School Students and Staff</p>
  <a class="btn-solid" href="#">GET STARTED</a>
  <div class="hero-curve"></div>
</section>

<section class="product-intro">
  <div class="product-logo"><span class="mark"></span>DeskRoute</div>
  <div class="intro-copy">
    <p>Lorem ipsum dolor sit amet, consectetur adipiscing elit, sed do eiusmod tempor incididunt ut labore et dolore magna aliqua. Ut enim ad minim veniam, quis nostrud exercitation ullamco laboris nisi ut aliquip ex ea commodo consequat</p>
    <p>Sed ut perspiciatis unde omnis iste natus error sit voluptatem accusantium doloremque laudantium, totam rem aperiam, eaque ipsa quae ab illo inventore veritatis et quasi architecto beatae vitae dicta sunt explicabo. Nemo enim ipsam voluptatem quia voluptas sit aspernatur aut odit aut fugit, sed quia consequuntur magni dolores eos qui ratione voluptatem sequi nesciunt.</p>
  </div>
</section>

<section class="about">
  <div class="about-photo" role="img" aria-label="Photo of students working at classroom computers, tinted blue"></div>
  <h2>ABOUT US</h2>
  <p class="about-lead">We develop educational software for Middle and High School Students and Staff.</p>
  <a class="btn-outline" href="#">READ MORE</a>
</section>

<section class="pricing">
  <h2 class="section-title">DESKROUTE PRICING</h2>
  <article class="plan school">
    <div class="plan-head">Individual School Purchase</div>
    <div class="plan-price"><span class="amount">$200</span><span class="unit">per school</span></div>
    <ul class="plan-features">
      <li><svg width="11" height="11" viewBox="0 0 11 11"><circle cx="5.5" cy="5.5" r="5.5" fill="#c8202e"/><path d="M3 5.6l1.7 1.7L8 4" fill="none" stroke="#fff" stroke-width="1.4"/></svg>12 months of access to DeskRoute.</li>
      <li><svg width="11" height="11" viewBox="0 0 11 11"><circle cx="5.5" cy="5.5" r="5.5" fill="#c8202e"/><path d="M3 5.6l1.7 1.7L8 4" fill="none" stroke="#fff" stroke-width="1.4"/></svg>Individual Accounts for each school Counselor in your office.</li>
      <li><svg width="11" height="11" viewBox="0 0 11 11"><circle cx="5.5" cy="5.5" r="5.5" fill="#c8202e"/><path d="M3 5.6l1.7 1.7L8 4" fill="none" stroke="#fff" stroke-width="1.4"/></svg>Customizable Student Login screen.</li>
      <li><svg width="11" height="11" viewBox="0 0 11 11"><circle cx="5.5" cy="5.5" r="5.5" fill="#c8202e"/><path d="M3 5.6l1.7 1.7L8 4" fill="none" stroke="#fff" stroke-width="1.4"/></svg>Access to a variety of Data Reports in Excel and PDF format.</li>
      <li><svg width="11" height="11" viewBox="0 0 11 11"><circle cx="5.5" cy="5.5" r="5.5" fill="#c8202e"/><path d="M3 5.6l1.7 1.7L8 4" fill="none" stroke="#fff" stroke-width="1.4"/></svg>Email Product Support.</li>
    </ul>
  </article>
  <article class="plan district">
    <div class="plan-head">District Level Purchase</div>
    <div class="plan-price"><span class="amount">$150</span><span class="unit">per school</span></div>
    <ul class="plan-features">
      <li><svg width="11" height="11" viewBox="0 0 11 11"><circle cx="5.5" cy="5.5" r="5.5" fill="#c8202e"/><path d="M3 5.6l1.7 1.7L8 4" fill="none" stroke="#fff" stroke-width="1.4"/></svg>12 months of access to DeskRoute for each school.</li>
      <li><svg width="11" height="11" viewBox="0 0 11 11"><circle cx="5.5" cy="5.5" r="5.5" fill="#c8202e"/><path d="M3 5.6l1.7 1.7L8 4" fill="none" stroke="#fff" stroke-width="1.4"/></svg>District level access to information and reports.</li>
      <li><svg width="11" height="11" viewBox="0 0 11 11"><circle cx="5.5" cy="5.5" r="5.5" fill="#c8202e"/><path d="M3 5.6l1.7 1.7L8 4" fill="none" stroke="#fff" stroke-width="1.4"/></svg>District level Account Controls.</li>
      <li><svg width="11" height="11" viewBox="0 0 11 11"><circle cx="5.5" cy="5.5" r="5.5" fill="#c8202e"/><path d="M3 5.6l1.7 1.7L8 4" fill="none" stroke="#fff" stroke-width="1.4"/></svg>Access to a variety of Data Reports in Excel and PDF format.</li>
      <li><svg width="11" height="11" viewBox="0 0 11 11"><circle cx="5.5" cy="5.5" r="5.5" fill="#c8202e"/><path d="M3 5.6l1.7 1.7L8 4" fill="none" stroke="#fff" stroke-width="1.4"/></svg>Email Product Support.</li>
    </ul>
  </article>
</section>

<section class="faq">
  <h2 class="section-title">DESKROUTE FAQS</h2>
  <div class="faq-col what">
    <div class="faq-label"><span class="qbox">?</span>What</div>
    <p class="faq-q">What is DeskRoute?</p>
    <p class="faq-a">DeskRoute is an electronic sign in system that replaces your old fashioned clipboard.</p>
    <p class="faq-q">What do I need in order to run DeskRoute?</p>
    <p class="faq-a">You need a computer, laptop or tablet and an internet connection.</p>
  </div>
  <div class="faq-col why">
    <div class="faq-label"><span class="qbox">?</span>Why</div>
    <p class="faq-q">Why should I buy DeskRoute?</p>
    <p class="faq-a">Lorem ipsum dolor sit amet, consectetur adipiscing elit, sed do eiusmod tempor incididunt ut labore et dolore magna.</p>
    <p class="faq-a">Duis aute irure dolor in reprehenderit in voluptate velit esse cillum dolore eu fugiat nulla pariatur.</p>
  </div>
  <div class="faq-col how">
    <div class="faq-label"><span class="qbox">?</span>How</div>
    <p class="faq-q">How much does it cost?</p>
    <p class="faq-a">Lorem ipsum dolor sit amet, consectetur adipiscing elit, sed do eiusmod tempor incididunt ut labore et dolore magna aliqua. Ut enim ad minim veniam, quis nostrud exercitation ullamco laboris nisi ut aliquip ex ea commodo consequat.</p>
  </div>
  <div class="faq-col who">
    <div class="faq-label"><span class="qbox">?</span>Who</div>
    <p class="faq-q">Who can view information in DeskRoute?</p>
    <p class="faq-a">Lorem ipsum dolor sit amet, consectetur adipiscing elit, sed do eiusmod tempor incididunt ut labore et dolore magna aliqua. Ut enim ad minim veniam, quis nostrud exercitation ullamco laboris nisi.</p>
  </div>
</section>

<footer class="site-footer">
  <div class="footer-col col-links">
    <h4>Links</h4>
    <ul><li>Home</li><li>About us</li><li>Our services</li><li>Blog</li><li>Partners</li><li>Contact us</li></ul>
  </div>
  <div class="footer-col col-news">
    <h4>Join our newsletter</h4>
    <p>Alternatively, please fill out the form below to contact me via email.</p>
    <div class="news-input">Enter Your Email</div>
    <div class="news-btn">SUBSCRIBE</div>
  </div>
  <div class="footer-divider" style="left:560px"></div>
  <div class="footer-col col-info">
    <h4>Information</h4>
    <ul><li>Terms &amp; Conditions</li><li>Privacy policy</li><li>Disclaimer</li><li>Contact us</li><li>Sitemap</li></ul>
  </div>
  <div class="footer-col col-why">
    <h4>Why us</h4>
    <ul><li>Customers</li><li>Team</li><li>FAQ</li><li>News</li><li>Others</li></ul>
  </div>
  <div class="footer-col col-contact">
    <h4>Contact info</h4>
    <ul>
      <li>RJ SYSTEMWORKS</li>
      <li class="indent">22 Street Name</li>
      <li class="indent">City Name, Country</li>
      <li><svg width="11" height="11" viewBox="0 0 11 11"><path d="M2 1h2l1 2.5-1.3 1a6 6 0 0 0 2.8 2.8l1-1.3L10 7v2a1 1 0 0 1-1 1A8 8 0 0 1 1 2a1 1 0 0 1 1-1z" fill="#c9c9cc"/></svg>01234 567 89</li>
      <li><svg width="12" height="9" viewBox="0 0 12 9"><rect width="12" height="9" fill="#c9c9cc"/><path d="M0 0l6 5 6-5" fill="none" stroke="#3d3d40" stroke-width="1.2"/></svg>info@rjsystemworks.net</li>
    </ul>
  </div>
</footer>

<div class="footer-bar">
  <span class="copy">© 2017. RJ Systemworks. All rights reserved</span>
  <div class="social">
    <span>Connect with our social network :</span>
    <span class="dot"></span><span class="dot"></span><span class="dot"></span><span class="dot"></span><span class="dot"></span>
  </div>
</div>

</body>
</html>
```